IT business looking for Standout Letterhead Design

We need a letterhead design for a company based in Bayport, CA called Corvane Systems, Inc. We specialize in IT engineering, installation and technical support pertaining to the department of defense.

We would like to see a design that incorporates the black and gold that matches our company logo.

More information on the company can be found at www.corvane-sys.example

```html
<!DOCTYPE html>
<html lang="en">
<head>
<meta charset="utf-8">
<title>Corvane Systems, Inc. — Letterhead</title>
<link rel="stylesheet" href="https://fonts.googleapis.com/css2?family=Cinzel:wght@400&family=Open+Sans:wght@400&display=swap">
<style>
  :root {
    --ink: #0d0d0d;
    --paper: #ffffff;
    --gold-deep: #a8641e;
    --gold-mid: #d9a531;
    --gold-bright: #f2e236;
    --contact-text: #ffffff;
  }
  html, body {
    margin: 0;
    padding: 0;
    width: 963px;
    height: 1200px;
    overflow: hidden;
    background: var(--paper);
  }
  .letterhead {
    position: relative;
    width: 963px;
    height: 1200px;
    background: var(--paper);
    overflow: hidden;
  }
  .header-band {
    position: absolute;
    top: 0;
    left: 0;
    width: 963px;
    height: 180px;
  }
  .company-name {
    position: absolute;
    left: 62px;
    top: 104px;
    margin: 0;
    font-family: "Cinzel", serif;
    font-weight: 400;
    font-size: 30px;
    letter-spacing: 0.5px;
    color: var(--ink);
    line-height: 1;
  }
  .contact-list {
    position: absolute;
    top: 18px;
    right: 18px;
    margin: 0;
    padding: 0;
    list-style: none;
    font-family: "Open Sans", sans-serif;
    font-size: 15px;
    color: var(--contact-text);
    text-align: right;
  }
  .contact-list li {
    display: flex;
    justify-content: flex-end;
    align-items: center;
    gap: 6px;
    height: 24px;
  }
  .contact-icon {
    width: 13px;
    height: 13px;
    flex: none;
  }
  .watermark-area {
    position: absolute;
    left: 0;
    top: 410px;
    width: 870px;
    height: 700px;
    background: radial-gradient(ellipse at 35% 55%, rgba(228,228,228,0.6) 0%, rgba(240,240,240,0.35) 45%, rgba(255,255,255,0) 72%);
  }
  .footer-rule {
    position: absolute;
    left: 0;
    bottom: 0;
    width: 963px;
    height: 22px;
  }
</style>
</head>
<body>
<main class="letterhead">

  <svg class="header-band" viewBox="0 0 963 180" aria-hidden="true">
    <defs>
      <linearGradient id="goldRule" x1="0" y1="0" x2="1" y2="0">
        <stop offset="0" stop-color="var(--gold-deep)"/>
        <stop offset="0.5" stop-color="var(--gold-bright)"/>
        <stop offset="1" stop-color="var(--gold-deep)"/>
      </linearGradient>
    </defs>
    <polygon points="680,0 963,0 963,150 640,150" fill="var(--ink)"/>
    <rect x="0" y="164" width="963" height="3" fill="url(#goldRule)"/>
  </svg>

  <h1 class="company-name">Corvane Systems, Inc.</h1>

  <ul class="contact-list">
    <li>Bayport, CA
      <svg class="contact-icon" viewBox="0 0 12 12"><path d="M6 0.5a4 4 0 0 0-4 4c0 3 4 7 4 7s4-4 4-7a4 4 0 0 0-4-4z" fill="#fff"/><circle cx="6" cy="4.5" r="1.5" fill="#0d0d0d"/></svg>
    </li>
    <li>619-555-0142
      <svg class="contact-icon" viewBox="0 0 12 12"><circle cx="6" cy="6" r="5.2" fill="none" stroke="#fff" stroke-width="1"/><path d="M4 3.2l1.2 1.4-.6.8c.4.9 1 1.5 1.9 1.9l.8-.6 1.4 1.2-.8 1c-2.4-.4-4.1-2.1-4.6-4.6z" fill="#fff"/></svg>
    </li>
    <li>619-555-0187
      <svg class="contact-icon" viewBox="0 0 12 12"><rect x="3" y="1.5" width="6" height="3" fill="#fff"/><rect x="1" y="4.5" width="10" height="5" rx="1" fill="#fff"/><rect x="3" y="7" width="6" height="3.5" fill="#0d0d0d" stroke="#fff" stroke-width="0.8"/></svg>
    </li>
    <li>info@corvane-sys.example
      <svg class="contact-icon" viewBox="0 0 12 12"><rect x="1" y="3" width="10" height="7" rx="1" fill="#fff"/><path d="M1.5 3.5L6 7l4.5-3.5" fill="none" stroke="#0d0d0d" stroke-width="1"/></svg>
    </li>
    <li>www.corvane-sys.example
      <svg class="contact-icon" viewBox="0 0 12 12"><circle cx="6" cy="6" r="5" fill="none" stroke="#fff" stroke-width="1"/><ellipse cx="6" cy="6" rx="2.2" ry="5" fill="none" stroke="#fff" stroke-width="0.9"/><path d="M1 6h10M2 3.5h8M2 8.5h8" stroke="#fff" stroke-width="0.8"/></svg>
    </li>
  </ul>

  <div class="watermark-area" role="img" aria-label="Faint oversized company mark watermark in light grey"></div>

  <svg class="footer-rule" viewBox="0 0 963 22" preserveAspectRatio="none" aria-hidden="true">
    <defs>
      <linearGradient id="footerGold" x1="0" y1="0" x2="1" y2="0">
        <stop offset="0" stop-color="var(--gold-deep)"/>
        <stop offset="0.5" stop-color="var(--gold-bright)"/>
        <stop offset="1" stop-color="var(--gold-deep)"/>
      </linearGradient>
    </defs>
    <rect x="0" y="0" width="963" height="3" fill="url(#footerGold)"/>
    <rect x="0" y="8" width="963" height="14" fill="var(--ink)"/>
  </svg>

</main>
</body>
</html>
```